Brochure Design Project

We are a Professional Employer Organization. We save employers time and money on workers' compensation, payroll and benefits.

```html
<!DOCTYPE html>
<html lang="en">
<head>
<meta charset="utf-8">
<title>Harbor PEO Brochure</title>
<link href="https://fonts.googleapis.com/css2?family=Oswald:wght@400;500;600&family=Tinos:wght@400;700&family=Arimo:wght@400;700&display=swap" rel="stylesheet">
<style>
  :root{
    --ink:#262a33;
    --orange:#f29a1e;
    --orange-deep:#e8890f;
    --grey-dark:#4c4f55;
    --grey-mid:#7d8086;
    --white:#ffffff;
    --sky:#5fd0ef;
    --text:#2a2a2a;
  }
  *{margin:0;padding:0;box-sizing:border-box}
  html,body{width:1200px;height:1000px;overflow:hidden;background:var(--white)}
  .brochure{position:relative;width:1200px;height:1000px;background:var(--white);font-family:"Tinos",serif;color:var(--text)}
  .bands{position:absolute;left:0;top:0}
  .abs{position:absolute}

  .brand-name{left:214px;top:122px;font-family:"Oswald",sans-serif;font-weight:500;font-size:60px;line-height:1;color:var(--orange);letter-spacing:0}
  .brand-sub{left:218px;top:183px;font-family:"Arimo",sans-serif;font-size:15px;color:var(--ink)}

  .team-visual{left:84px;top:212px}
  .strategy-visual{left:445px;top:110px}
  .growth-photo{left:805px;top:145px;width:343px;height:370px;border-radius:0 10px 0 0;
    background:linear-gradient(135deg,#c9ccd2 0%,#8d929b 35%,#2d3139 70%,#1d2027 100%)}

  .selecting-box{left:42px;top:413px;width:286px;height:57px;background:var(--ink);color:var(--white);
    font-family:"Oswald",sans-serif;font-weight:500;font-size:44px;line-height:57px;padding-left:10px;letter-spacing:-0.5px}
  .selecting-tag{left:42px;top:476px;width:178px;height:29px;background:var(--orange);color:var(--white);
    font-family:"Arimo",sans-serif;font-size:22px;line-height:29px;padding-left:12px}
  .selecting-rule{left:42px;top:512px;width:58px;height:4px;background:var(--orange)}
  .intro{left:65px;top:518px;width:340px;font-size:16px;line-height:20.5px}
  .intro p{margin-bottom:20px}
  .intro .narrow{width:248px;text-align:justify;text-align-last:left}

  .focus-title{left:453px;top:420px;font-weight:700;font-size:46px;line-height:1;color:var(--orange)}
  .focus-sub{left:453px;top:467px;font-family:"Arimo",sans-serif;font-size:20px;line-height:24px;color:var(--ink)}
  .focus-bar{left:655px;top:495px;width:150px;height:20px;background:var(--orange)}
  .services{left:453px;top:526px;list-style:none;font-size:13.8px;line-height:17.1px}

  .succeed{left:810px;top:553px;width:370px;font-weight:700;color:var(--ink);font-size:18px;line-height:28.6px}
  .succeed .lead{color:var(--orange);font-size:29px}

  .contact{color:var(--white);font-weight:700}
  .call-today{left:195px;top:795px;display:flex;align-items:center;gap:4px;font-size:18px}
  .call-number{left:208px;top:829px;font-size:27px;color:var(--orange)}
  .consult{left:455px;top:791px;width:300px;text-align:center;font-size:13px;line-height:19px}
  .consult .row{display:flex;justify-content:center;align-items:center;gap:8px}
  .send-icon{left:798px;top:800px}
  .right-contact{left:862px;top:792px;width:270px;text-align:center;font-size:25px;line-height:36px}
</style>
</head>
<body>
<div class="brochure">

  <svg class="bands" width="1200" height="1000" viewBox="0 0 1200 1000">
    <path d="M0 75 H1200 V182 H215 Q190 182 180 198 L172 208 L164 198 Q154 182 130 182 H0 Z" fill="var(--ink)"/>
    <path d="M0 780 H990 Q1010 780 1018 765 L1026 752 L1034 765 Q1042 780 1062 780 H1200 V922 H0 Z" fill="var(--ink)"/>
  </svg>

  <div class="abs brand-name">HARBOR</div>
  <div class="abs brand-sub">Employee Management, Inc</div>

  <svg class="abs team-visual" width="180" height="180" viewBox="0 0 180 180">
    <path d="M88 0 A88 88 0 1 0 132 164 L140 176 L138 150 A88 88 0 0 0 88 0 Z" fill="var(--grey-dark)"/>
    <circle cx="88" cy="88" r="70" fill="var(--grey-mid)"/>
    <circle cx="88" cy="88" r="55" fill="var(--white)"/>
    <circle cx="88" cy="90" r="47" fill="#e8eef3" role="img" aria-label="Illustration of business people shaking hands over gears"/>
  </svg>

  <svg class="abs strategy-visual" width="310" height="300" viewBox="0 0 310 300">
    <defs>
      <radialGradient id="strategyTone" cx="0.45" cy="0.4" r="0.7">
        <stop offset="0" stop-color="#bfe0ea"/>
        <stop offset="0.6" stop-color="#3d8ea6"/>
        <stop offset="1" stop-color="#1f4f63"/>
      </radialGradient>
    </defs>
    <circle cx="153" cy="150" r="146" fill="var(--orange)"/>
    <path d="M8 150 A146 146 0 0 1 153 4 A146 146 0 0 0 8 150 Z" fill="var(--orange)"/>
    <path d="M200 20 A140 140 0 0 1 292 170 A146 146 0 0 1 160 296 A150 150 0 0 0 200 20 Z" fill="var(--orange-deep)" opacity="0.6"/>
    <path d="M140 250 L148 278 L168 258 Z" fill="var(--orange-deep)"/>
    <circle cx="155" cy="158" r="104" fill="url(#strategyTone)" role="img" aria-label="Photo of 3D business words: strategy, budget, team, analysis"/>
  </svg>

  <div class="abs growth-photo" role="img" aria-label="Photo of a businessman touching a rising growth chart"></div>

  <div class="abs selecting-box">BY SELECTING</div>
  <div class="abs selecting-tag">HARBOR PEO</div>
  <div class="abs selecting-rule"></div>
  <div class="abs intro">
    <p>You establish a co-employer Relationship.<br>Harbor takes on the administrative responsibility<br>of managing your employees.</p>
    <p>Our all-inclusive program includes<br>The preparation and filing of Payroll taxes,<br>benefit administration, workers’ compensation<br>and federal and state unemployment.</p>
    <p class="narrow">We work with you to ensure em-<br>ployee Related governmental com-<br>pliance.</p>
  </div>

  <div class="abs focus-title">You focus</div>
  <div class="abs focus-sub">on running your business<br>and we take care of:</div>
  <div class="abs focus-bar"></div>
  <ul class="abs services">
    <li>- Paycheck Calculations</li>
    <li>- Record keeping</li>
    <li>- Weekly, Monthly, Quarterly Tax Deposits</li>
    <li>- Quarterly Tax Reporting</li>
    <li>- New Hire Reporting</li>
    <li>- INS Compliance</li>
    <li>- IRS Compliance</li>
    <li>- DOL Compliance</li>
    <li>- W2 and W3</li>
    <li>- Child Supports and Garnishment Administration</li>
    <li>- Banking and Direct Deposits</li>
    <li>- Wage Verifications</li>
    <li>- Unemployment Claims</li>
    <li>- Workers’ Compensation Audits</li>
  </ul>

  <div class="abs succeed">
    <span class="lead">Let Harbor</span> help you succeed<br>
    By reducing employer overhead<br>
    (insurance and taxes) while<br>
    Simplifying employee administration,<br>
    Ensuring governmental compliance,<br>
    And increasing employee benefits.
  </div>

  <div class="abs contact call-today">
    <svg width="30" height="30" viewBox="0 0 30 30"><circle cx="15" cy="15" r="13" fill="none" stroke="var(--orange)" stroke-width="2"/><path d="M11 8 l3 3 -2 2 q2 4 5 5 l2 -2 3 3 -2 2 q-8 -1 -11 -11 z" fill="var(--orange)"/></svg>
    <span>CALL TODAY</span>
  </div>
  <div class="abs contact call-number">844-555-0139</div>

  <div class="abs contact consult">
    <div>CALL FOR A FREE CONSULTATION</div>
    <div class="row">
      <svg width="18" height="18" viewBox="0 0 18 18"><circle cx="9" cy="9" r="8" fill="none" stroke="var(--orange)" stroke-width="1.4"/><path d="M6 4 l2 2 -1 1.5 q1 2.5 3.5 3.5 l1.5 -1 2 2 -1.5 1.5 q-5 -1 -7 -7 z" fill="var(--orange)"/></svg>
      <span>844-555-0139</span>
    </div>
    <div>OR VISIT OUR WEBSITE AT</div>
    <div class="row">
      <svg width="18" height="18" viewBox="0 0 18 18" fill="none" stroke="var(--orange)" stroke-width="1.3"><circle cx="9" cy="9" r="7.5"/><ellipse cx="9" cy="9" rx="3.5" ry="7.5"/><path d="M1.5 9 H16.5 M3 5 H15 M3 13 H15"/></svg>
      <span>www.HARBORPEO.com</span>
    </div>
  </div>

  <svg class="abs send-icon" width="58" height="58" viewBox="0 0 58 58">
    <circle cx="28" cy="28" r="28" fill="var(--sky)"/>
    <path d="M15 29 L41 17 L34 41 L27 33 Z M27 33 L41 17" fill="none" stroke="var(--white)" stroke-width="2" stroke-linejoin="round"/>
  </svg>
  <div class="abs contact right-contact">844-555-0139<br>www.HARBORPEO.com</div>

</div>
</body>
</html>
```